Harbor Petroleum Business Cards

I would like to design some options for about 10 sets of double sided business cards for our team with a raised logo with a Silver glossy finished logo. We are a privately funded upstream Oil & Gas producer drilling vertical wells in Central Oklahoma with a long term production (ROI driven) strategy that we implement through an annual drilling program. We are focused on a shallow / vertical / long life / low decline strategy. We are based in downtown Tulsa Oklahoma. I have attached a sample business card and a picture of our hallway logo which we would like to replicate on the business cards.

Target Market(s)

SEC Accredited Investors and other Oil & Gas Operators

Industry/Entity Type

Upstream Oil & Gas

Contact Information for Business Card

You can see the sample photo attached, but email / website / address / direct phone / Cell Phone / Name / Title / Fax

Font styles to use
Other font styles liked:
• Felix Titling

Colors
0054AA
0677BA
7BADD7
CADEEF
E8F1F8

Requirements
Must have
• Glossy raised logo
Nice to have
• Possibly a new logo.
Should not have
• No Greens /

```html
<!DOCTYPE html>
<html lang="en">
<head>
<meta charset="utf-8">
<title>Harbor Petroleum Business Cards</title>
<link href="https://fonts.googleapis.com/css2?family=Cinzel:wght@400;600&display=swap" rel="stylesheet">
<style>
  :root {
    --backdrop: #b3b3b3;
    --card: #ffffff;
    --brand-grey: #555555;
    --mark-grey: #8c8c8c;
    --ink: #111111;
    --band: #000000;
    --band-text: #ffffff;
  }
  * { margin: 0; padding: 0; box-sizing: border-box; }
  html, body {
    width: 1200px; height: 457px; overflow: hidden;
    background: var(--backdrop);
    font-family: "Cinzel", serif;
  }
  .canvas { position: relative; width: 1200px; height: 457px; }
  .card {
    position: absolute; top: 88px;
    width: 494px; height: 282px;
    background: var(--card);
    overflow: hidden;
  }
  .card--front { left: 89px; }
  .card--back { left: 616px; }

  .brand-mark { position: absolute; display: block; }
  .brand-mark circle { fill: var(--mark-grey); }
  .card--front .brand-mark { left: 207px; top: 26px; width: 80px; height: 80px; }
  .card--back .brand-mark { left: 189px; top: 56px; width: 116px; height: 116px; }

  .brand-name {
    position: absolute; left: 0; right: 0;
    text-align: center; color: var(--brand-grey);
    font-weight: 400; white-space: nowrap; text-transform: uppercase;
  }
  .card--front .brand-name { top: 124px; font-size: 18px; }
  .card--back .brand-name { top: 198px; font-size: 26px; }

  .person-name {
    position: absolute; left: 0; right: 0; top: 148px;
    text-align: center; color: var(--ink);
    font-size: 21px; font-weight: 400; white-space: nowrap; text-transform: uppercase;
  }
  .person-title {
    position: absolute; left: 0; right: 0; top: 178px;
    text-align: center; color: var(--ink);
    font-size: 8.5px; line-height: 11px; text-transform: uppercase;
  }
  .contact-phones {
    position: absolute; left: 80px; top: 203px;
    font-size: 11.5px; line-height: 14.5px; color: var(--ink);
    list-style: none; text-transform: uppercase;
  }
  .contact-address {
    position: absolute; left: 304px; width: 134px; top: 203px;
    text-align: center; font-style: normal;
    font-size: 11.5px; line-height: 14.5px; color: var(--ink); text-transform: uppercase;
  }
  .contact-email {
    position: absolute; left: 0; right: 0; top: 248px;
    text-align: center; font-size: 11px; color: var(--ink); text-transform: uppercase;
  }
  .web-band {
    position: absolute; left: 0; right: 0; bottom: 0; height: 20px;
    background: var(--band); color: var(--band-text);
    font-size: 10px; line-height: 20px; text-align: center; text-transform: uppercase;
  }
</style>
</head>
<body>
<main class="canvas">
  <section class="card card--front" aria-label="Business card front">
    <svg class="brand-mark" viewBox="0 0 80 80" role="img" aria-label="Raised silver company logo mark">
      <circle cx="40" cy="40" r="40"/>
    </svg>
    <p class="brand-name">Harbor Petroleum, LLC</p>
    <h1 class="person-name">Dorian K. Wexford, CPL</h1>
    <p class="person-title">Executive Vice President<br>Land, Legal &amp; Business Development</p>
    <ul class="contact-phones">
      <li>D: 539-555-0142</li>
      <li>C: 918-555-0187</li>
      <li>F: 918-555-0163</li>
    </ul>
    <address class="contact-address">42 West 9th St<br>Suite 800<br>Tulsa, OK 74103</address>
    <p class="contact-email">dkw@hptulsa.com</p>
    <p class="web-band">www.harborpetroleumllc.com</p>
  </section>

  <section class="card card--back" aria-label="Business card back">
    <svg class="brand-mark" viewBox="0 0 116 116" role="img" aria-label="Raised silver company logo mark">
      <circle cx="58" cy="58" r="58"/>
    </svg>
    <p class="brand-name">Harbor Petroleum, LLC</p>
  </section>
</main>
</body>
</html>
```